Ridgeline Outfitters Business Cards

Recently had a logo done with Artfolio and now looking for a business card to go along with it.

Target Market(s)

Ridgeline Outfitters is a weapons dealer. My market will be primarily men, hunting, shooting type.

Industry/Entity Type

Business

Contact Information for Business Card

I selected double sided, but this is not required, single or double is going to be fine. I picture the logo on one side, or perhaps just the circle which contains "RO" with the remaining info on the other side.

Font styles to use
Sans Serif

Requirements
Must have
• My name: Milo Brandt
• Title: Owner
• tel: 612-555-0187
• web: www.ridgelineoutfittersmn.example
Nice to have
• I like the concept of a black business card. I would like to keep the colors monotone, black, grey, white or red. Red is acceptable because it is in the logo. I have also seen cards that are matte black with shiny black as well, perhaps for the logo (or circle RO) part of the logo.
• I will upload a couple of the logos for use, and also an example I just found of the black on black. and some others that have a nice contrast.
Should not have
• lots of colors are not wanted.

```html
<!DOCTYPE html>
<html lang="en">
<head>
<meta charset="utf-8">
<title>Ridgeline Outfitters Business Cards</title>
<link rel="stylesheet" href="https://fonts.googleapis.com/css2?family=Open+Sans:wght@400;600&display=swap">
<style>
  :root {
    --backdrop: #3b3431;
    --card: #141414;
    --card-edge: #1d1d1d;
    --gloss: #2c2c2c;
    --ink: #f4f4f4;
    --ink-soft: #d9d9d9;
  }
  * { margin: 0; padding: 0; box-sizing: border-box; }
  html, body {
    width: 1200px; height: 716px; overflow: hidden;
    background: var(--backdrop);
    font-family: "Open Sans", sans-serif;
  }
  .canvas { position: relative; width: 1200px; height: 716px; }
  .card {
    position: absolute; top: 210px;
    width: 520px; height: 297px;
    background: var(--card);
    border: 1px solid var(--card-edge);
    border-radius: 3px;
    box-shadow: 0 14px 30px rgba(0,0,0,.45);
  }
  .card--front { left: 60px; }
  .card--back { left: 620px; }

  .brand { position: absolute; display: flex; align-items: center; gap: 16px; }
  .brand__mark {
    width: 84px; height: 84px; border-radius: 50%;
    border: 7px solid currentColor; flex: none;
  }
  .brand__name {
    font-weight: 600; font-size: 23px; letter-spacing: 1px;
    text-transform: uppercase; white-space: nowrap;
  }
  .card--front .brand { left: 36px; top: 80px; color: var(--gloss); }
  .card--back .brand { left: 60px; top: 34px; color: var(--ink); }
  .card--back .brand__mark { width: 76px; height: 76px; border-width: 6px; }
  .card--back .brand__name { font-size: 21px; }

  .person { position: absolute; left: 38px; top: 168px; color: var(--ink); }
  .person__name { font-size: 20px; font-weight: 400; }
  .person__title { font-size: 14px; color: var(--ink-soft); margin-top: 2px; }

  .divider {
    position: absolute; left: 240px; top: 170px;
    width: 2px; height: 86px; background: var(--ink);
  }
  .contacts { position: absolute; left: 258px; top: 188px; list-style: none; color: var(--ink); }
  .contacts__item { display: flex; align-items: center; gap: 8px; font-size: 13px; margin-bottom: 14px; white-space: nowrap; }
  .contacts__icon { width: 14px; height: 14px; flex: none; }
</style>
</head>
<body>
<main class="canvas">
  <section class="card card--front" aria-label="Card front">
    <div class="brand">
      <span class="brand__mark"></span>
      <span class="brand__name">Ridgeline Outfitters</span>
    </div>
  </section>

  <section class="card card--back" aria-label="Card back">
    <div class="brand">
      <span class="brand__mark"></span>
      <span class="brand__name">Ridgeline Outfitters</span>
    </div>
    <div class="person">
      <p class="person__name">Milo Brandt</p>
      <p class="person__title">Owner</p>
    </div>
    <span class="divider"></span>
    <ul class="contacts">
      <li class="contacts__item">
        <svg class="contacts__icon" viewBox="0 0 14 14" aria-hidden="true">
          <rect width="14" height="14" rx="2" fill="#f4f4f4"/>
          <path d="M4 3.5c.6-.5 1.2-.3 1.5.3l.5 1c.2.5 0 .8-.4 1.1.4.9 1 1.5 1.9 1.9.3-.4.6-.6 1.1-.4l1 .5c.6.3.8.9.3 1.5-1.6 1.7-6.9-3.6-5.9-5.9z" fill="#141414"/>
        </svg>
        612-555-0187
      </li>
      <li class="contacts__item">
        <svg class="contacts__icon" viewBox="0 0 14 14" aria-hidden="true">
          <rect width="14" height="14" rx="2" fill="#f4f4f4"/>
          <circle cx="7" cy="7" r="4" fill="none" stroke="#141414" stroke-width="1"/>
          <path d="M3 7h8M7 3c-1.6 2.4-1.6 5.6 0 8M7 3c1.6 2.4 1.6 5.6 0 8" fill="none" stroke="#141414" stroke-width=".8"/>
        </svg>
        www.ridgelineoutfittersmn.example
      </li>
    </ul>
  </section>
</main>
</body>
</html>
```